Request for Business Card Design

Hi. My name is Marlena, I am looking for a new business card design for my company, Quillbrook Sensing Systems, LLC. I really like the design you did for Tavel Harvest and was hoping you could do something similar using our full logo and our mark. I am also open to any raised texture design using our mark. I have attached our full logo, which would need to be somewhere on the card, as well as the mark in both outline and full form, as well as our brand colors / guide. The card does not have to be white, as long as our logo and mark appear. I actually like darker colored business cards more, but am open to all options. If you are interested in working with me, please let me know. We would also take the business card design into letterhead design if you can do that.

```html
<!DOCTYPE html>
<html lang="en">
<head>
<meta charset="utf-8">
<title>Quillbrook Sensing Systems — Business Card</title>
<link rel="stylesheet" href="https://fonts.googleapis.com/css2?family=Montserrat:wght@400;500&family=Barlow:wght@600&display=swap">
<style>
  :root {
    --stage: #3a3b3d;
    --card-black: #1c1c1d;
    --card-black-light: #2a2a2b;
    --paper: #ffffff;
    --brand-blue: #0aa0c8;
    --ink-light: #f2f2f2;
  }
  * { box-sizing: border-box; margin: 0; padding: 0; }
  html, body {
    width: 1200px; height: 1200px; overflow: hidden;
    background: var(--stage);
  }
  .canvas {
    position: relative; width: 1200px; height: 1200px;
  }
  .card {
    position: absolute; left: 180px; width: 840px; height: 480px;
    border-radius: 36px; overflow: hidden;
    box-shadow: 0 4px 0 var(--brand-blue), 0 14px 30px rgba(0,0,0,.45);
  }
  .card--front { top: 80px; background: var(--card-black); }
  .card--back {
    top: 640px;
    background: linear-gradient(160deg, var(--card-black-light) 0%, var(--card-black) 60%);
  }
  .front-shapes { position: absolute; inset: 0; }

  .front-brand {
    position: absolute; left: 40px; top: 210px; width: 380px;
    display: flex; align-items: center; gap: 14px;
    font-family: "Barlow", sans-serif; font-weight: 600;
    font-size: 30px; color: var(--brand-blue); letter-spacing: .5px;
  }
  .brand-dot {
    width: 46px; height: 46px; border-radius: 50%;
    background: var(--brand-blue); flex: none;
  }

  .contact {
    position: absolute; left: 540px; top: 92px; width: 290px;
    font-family: "Montserrat", sans-serif; color: var(--ink-light);
  }
  .contact__name {
    font-size: 38px; font-weight: 500; color: var(--brand-blue);
    line-height: 1; letter-spacing: -.5px;
  }
  .contact__title { font-size: 24px; font-weight: 400; margin-top: 4px; }
  .contact__list { list-style: none; margin-top: 24px; }
  .contact__item {
    display: flex; align-items: flex-start; gap: 10px;
    font-size: 17px; line-height: 1.35; margin-bottom: 6px;
  }
  .contact__icon { width: 18px; height: 18px; flex: none; margin-top: 2px; }

  .back-brand {
    position: absolute; left: 0; right: 0; top: 0; bottom: 0;
    display: flex; align-items: center; justify-content: center; gap: 26px;
    font-family: "Barlow", sans-serif; font-weight: 600;
    font-size: 44px; color: var(--paper); letter-spacing: 2px;
    text-transform: uppercase;
  }
  .back-brand .brand-dot { width: 110px; height: 110px; }
</style>
</head>
<body>
<main class="canvas">

  <section class="card card--front" aria-label="Business card front">
    <svg class="front-shapes" viewBox="0 0 840 480" width="840" height="480" aria-hidden="true">
      <path d="M0 0 H300 C470 60 520 300 470 480 H0 Z" fill="var(--paper)"/>
      <path d="M330 14 C510 90 548 300 500 480 H478 C525 300 490 110 330 14 Z" fill="var(--brand-blue)"/>
    </svg>

    <div class="front-brand"><span class="brand-dot"></span>Quillbrook</div>

    <div class="contact">
      <p class="contact__name">FULL NAME</p>
      <p class="contact__title">TITLE</p>
      <ul class="contact__list">
        <li class="contact__item">
          <svg class="contact__icon" viewBox="0 0 24 24" aria-hidden="true"><path d="M6.6 10.8a15 15 0 0 0 6.6 6.6l2.2-2.2a1 1 0 0 1 1-.25 11.4 11.4 0 0 0 3.6.57 1 1 0 0 1 1 1V20a1 1 0 0 1-1 1A17 17 0 0 1 3 4a1 1 0 0 1 1-1h3.5a1 1 0 0 1 1 1c0 1.25.2 2.45.57 3.57a1 1 0 0 1-.25 1z" fill="var(--brand-blue)"/></svg>
          <span>(000) 000 0000</span>
        </li>
        <li class="contact__item">
          <svg class="contact__icon" viewBox="0 0 24 24" aria-hidden="true"><rect x="2" y="5" width="20" height="14" rx="1" fill="var(--brand-blue)"/><path d="M2 6l10 7 10-7" stroke="var(--card-black)" stroke-width="2" fill="none"/></svg>
          <span>email@company.com</span>
        </li>
        <li class="contact__item">
          <svg class="contact__icon" viewBox="0 0 24 24" aria-hidden="true"><circle cx="12" cy="12" r="9" fill="none" stroke="var(--brand-blue)" stroke-width="2"/><path d="M3 12h18M12 3c3 3 3 15 0 18M12 3c-3 3-3 15 0 18" fill="none" stroke="var(--brand-blue)" stroke-width="1.6"/></svg>
          <span>www.company.com</span>
        </li>
        <li class="contact__item">
          <svg class="contact__icon" viewBox="0 0 24 24" aria-hidden="true"><path d="M12 2a7 7 0 0 0-7 7c0 5 7 13 7 13s7-8 7-13a7 7 0 0 0-7-7z" fill="var(--brand-blue)"/><circle cx="12" cy="9" r="2.5" fill="var(--card-black)"/></svg>
          <span>123 Name Street, 000<br>Your City, 00000-000</span>
        </li>
      </ul>
    </div>
  </section>

  <section class="card card--back" aria-label="Business card back">
    <div class="back-brand"><span class="brand-dot"></span>Quillbrook Sensing Systems</div>
  </section>

</main>
</body>
</html>
```